Aisle signage for supermarket

Design Isle signs for Indian supermarket. Modern, Clear, legible. Would be nice to use our logo colours. Signs Will be double sided and measure 900mm width x 400mm height. Indian theme would be nice. Attached files shows description to go on each sign.
Font styles to use
Sans Serif
Colors
Designer to choose colors to be used in the design.

```html
<!DOCTYPE html>
<html lang="en">
<head>
<meta charset="utf-8">
<title>Aisle Sign 1</title>
<link href="https://fonts.googleapis.com/css2?family=Archivo+Black&display=swap" rel="stylesheet">
<style>
  :root {
    --leaf: #8dc63f;
    --leaf-deep: #7cb536;
    --forest: #036937;
    --paper: #ffffff;
    --backdrop: #3a3a3a;
  }
  html, body {
    margin: 0;
    padding: 0;
    width: 1200px;
    height: 750px;
    overflow: hidden;
    background: var(--backdrop);
  }
  .canvas {
    position: relative;
    width: 1200px;
    height: 750px;
  }
  .aisle-sign {
    position: absolute;
    left: 40px;
    top: 126px;
    width: 1120px;
    height: 498px;
    display: block;
  }
  .sign-base { fill: var(--leaf); }
  .category-band { fill: var(--paper); }
  .number-panel { fill: var(--forest); }
  .category-label {
    font-family: "Archivo Black", "Arial Black", sans-serif;
    font-size: 76px;
    fill: var(--forest);
  }
  .aisle-number {
    font-family: "Archivo Black", "Arial Black", sans-serif;
    font-size: 300px;
    fill: var(--paper);
  }
  .store-name {
    font-family: "Archivo Black", "Arial Black", sans-serif;
    font-size: 40px;
    fill: var(--paper);
    letter-spacing: 2px;
  }
</style>
</head>
<body>
<main class="canvas">
  <svg class="aisle-sign" viewBox="0 0 1350 600" xmlns="http://www.w3.org/2000/svg" aria-label="Aisle 1 sign: Biscuits / Cakes, Tea / Coffe, Savouries">
    <defs>
      <radialGradient id="ornament-tone" cx="50%" cy="50%" r="50%">
        <stop offset="0%" stop-color="var(--leaf-deep)" stop-opacity="0.9"/>
        <stop offset="100%" stop-color="var(--leaf-deep)" stop-opacity="0"/>
      </radialGradient>
    </defs>

    <rect class="sign-base" x="0" y="0" width="1350" height="600"/>

    <ellipse class="ornament-area" role="img" aria-label="Faint Indian mandala ornament" cx="475" cy="420" rx="300" ry="150" fill="url(#ornament-tone)"/>

    <g class="category-bands">
      <polygon class="category-band" points="0,66 965,66 932,179 0,179"/>
      <polygon class="category-band" points="0,189 929,189 896,302 0,302"/>
      <polygon class="category-band" points="0,312 893,312 860,425 0,425"/>
    </g>

    <polygon class="number-panel" points="975,66 1350,66 1350,425 870,425"/>

    <g class="category-labels">
      <text class="category-label" x="110" y="150" textLength="762" lengthAdjust="spacingAndGlyphs">BISCUITS / CAKES</text>
      <text class="category-label" x="112" y="273" textLength="528" lengthAdjust="spacingAndGlyphs">TEA / COFFE</text>
      <text class="category-label" x="110" y="397" textLength="475" lengthAdjust="spacingAndGlyphs">SAVOURIES</text>
    </g>

    <text class="aisle-number" x="1103" y="357" text-anchor="middle" textLength="116" lengthAdjust="spacingAndGlyphs">1</text>

    <text class="store-name" x="1103" y="520" text-anchor="middle" textLength="355" lengthAdjust="spacingAndGlyphs">TARANG GROCERS</text>
  </svg>
</main>
</body>
</html>
```